Harbor Zentrik needs a new Website Design

We need a WEB site landing page (/template) design, we currently have a company logo.We like the Valtor.com web designEnclosed is our company logo.Our Current website is https://www.harborzentrik.com.au/

1 page

```html
<!DOCTYPE html>
<html lang="en">
<head>
<meta charset="utf-8">
<title>Zentrik UC – White-Label Communications</title>
<link href="https://fonts.googleapis.com/css2?family=Montserrat:wght@300;400;500;600;700&display=swap" rel="stylesheet">
<style>
:root{
  --bg:#f2f8fd;
  --panel:#ffffff;
  --sky-soft:#e4f5fd;
  --blue:#3b7fd2;
  --blue-mid:#5aa9ea;
  --blue-deep:#2f6cc0;
  --ink:#2d333d;
  --muted:#7c8591;
  --orange-a:#f09a58;
  --orange-b:#f7cfa4;
}
*{margin:0;padding:0;box-sizing:border-box}
html,body{width:1200px;height:1200px;overflow:hidden;background:var(--bg);font-family:"Montserrat",sans-serif;color:var(--ink)}
.canvas{position:relative;width:1200px;height:1200px;overflow:hidden;background:var(--bg)}
.page{position:absolute;background:var(--panel);overflow:hidden;box-shadow:0 10px 40px rgba(80,150,210,.12)}
.page--back{left:500px;top:0;width:700px;height:1200px}
.page--top{left:499px;top:0;width:279px;height:66px;z-index:1}
.page--front{left:78px;top:66px;width:700px;height:1134px;z-index:2}
.abs{position:absolute}
.band{position:absolute;left:-50px;width:900px;background:var(--sky-soft);opacity:.7}
.hero-bg{position:absolute;left:0;top:0;width:700px;height:420px;background:linear-gradient(180deg,#bfe8fb,#d9f2fd);clip-path:polygon(0 0,100% 0,100% 278px,0 414px)}
.logo{left:36px;top:26px;display:flex;align-items:center;gap:6px;font-size:12px;font-weight:400;color:var(--blue)}
.logo i{width:9px;height:9px;border-radius:50%;background:var(--blue-mid);display:block}
.nav{left:352px;top:29px;display:flex;gap:13px;font-size:6px;font-weight:500;color:var(--blue);letter-spacing:.2px}
h1.hero-title{left:36px;top:134px;font-size:17.5px;line-height:22px;font-weight:700;color:var(--blue)}
.hero-sub{left:36px;top:189px;font-size:8.5px;line-height:17px;color:var(--blue-mid)}
.btn{position:absolute;width:99px;height:26px;border-radius:4px;background:linear-gradient(90deg,var(--orange-a),var(--orange-b));color:#fff;font-size:8.5px;font-weight:600;display:flex;align-items:center;justify-content:space-between;padding:0 10px}
.btn svg{width:18px;height:8px}
.illus{position:absolute;border-radius:50%;background:radial-gradient(circle at 40% 35%,#8fd3f7,#4ea6e6)}
.illus--tile{border-radius:22px;background:linear-gradient(135deg,#8ad3f6,#3e8fdc)}
.dot{position:absolute;border-radius:50%;background:#fff;opacity:.9}
.dot--b{background:var(--blue-mid)}
.section-lead{left:0;width:700px;top:438px;text-align:center;font-size:16.5px;line-height:22px;font-weight:700;color:var(--blue)}
.feature-title{font-size:16px;font-weight:700;color:var(--ink);white-space:nowrap}
.feature-sub{font-size:8.5px;color:var(--ink);white-space:nowrap}
.feature-body{font-size:5.4px;line-height:12.3px;color:var(--muted)}
.right{text-align:right}
.start{position:absolute;left:278px;top:1004px;width:422px;height:54px;background:linear-gradient(90deg,var(--orange-a),var(--orange-b));display:flex;align-items:center;gap:14px;padding-left:27px;color:#fff;font-size:17px;font-weight:700}
.foot-col{position:absolute;top:1088px;text-align:center;font-size:8.5px;line-height:13px;color:var(--ink)}
.foot-col ul{list-style:none;margin-top:20px;font-size:5.5px;line-height:13.5px;color:var(--blue)}
.foot-col .plain{color:var(--ink)}
</style>
</head>
<body>
<div class="canvas">

  <section class="page page--back">
    <div class="band" style="top:250px;height:120px;transform:rotate(-9deg)"></div>
    <div class="band" style="top:680px;height:110px;transform:rotate(-9deg)"></div>

    <a class="btn" style="left:509px;top:45px">See more<svg viewBox="0 0 18 8"><path d="M0 4h16M12 1l4 3-4 3" fill="none" stroke="#fff" stroke-width="1"/></svg></a>

    <h2 class="abs feature-title" style="left:96px;top:116px">Invoice &amp; Payment Platform</h2>
    <p class="abs feature-sub" style="left:96px;top:155px">All pieces in one for an assertive management</p>
    <p class="abs feature-body" style="left:96px;top:182px;width:200px">Ledgera Portal is a customer portal designed for integration with switches and has a friendly GUI that handles billing, allowing you to spend more time to SELL!</p>

    <div class="illus illus--tile" role="img" aria-label="Illustration of a phone with a payment card and dollar signs" style="left:430px;top:136px;width:164px;height:166px;border-radius:18px 60px 60px 18px"></div>

    <h2 class="abs feature-title right" style="right:93px;top:338px">Data Services</h2>
    <div class="abs feature-body right" style="right:93px;top:405px;line-height:12.4px">
      Data Networks * not all services available all areas<br>Fibre<br>Ethernet - Symmetrical upload and downloads<br>Nexline - choose from three Internet speeds all with unlimited downloads
    </div>
    <a class="btn" style="left:509px;top:485px">See more<svg viewBox="0 0 18 8"><path d="M0 4h16M12 1l4 3-4 3" fill="none" stroke="#fff" stroke-width="1"/></svg></a>

    <div class="illus illus--tile" role="img" aria-label="Illustration of a phone connected to support agents" style="left:424px;top:549px;width:174px;height:173px;border-radius:40px;background:linear-gradient(135deg,#5aa6e8,#2f6cc0)"></div>

    <h2 class="abs feature-title right" style="right:93px;top:779px">Support</h2>
    <p class="abs feature-sub right" style="right:93px;top:818px">We are here to help</p>
    <p class="abs feature-body right" style="right:93px;top:846px;width:260px">Our technical support team is always available to you via phone, live chat and support ticketing system.</p>
    <a class="btn" style="left:509px;top:925px">See more<svg viewBox="0 0 18 8"><path d="M0 4h16M12 1l4 3-4 3" fill="none" stroke="#fff" stroke-width="1"/></svg></a>

    <div class="start">Start<svg width="28" height="12" viewBox="0 0 28 12"><path d="M0 6h26M20 1l6 5-6 5" fill="none" stroke="#fff" stroke-width="1.6"/></svg></div>

    <div class="foot-col" style="left:299px;width:100px">Support /<br>Administration
      <ul><li>admin@harborzentrik.com.au</li><li class="plain">+61200004417</li></ul>
    </div>
    <div class="foot-col" style="left:431px;width:100px">Terms &amp; Conditions
      <ul style="margin-top:27px"><li>General Voice</li><li>Data</li><li>Porting &amp; Charges</li><li>International Calling</li></ul>
    </div>
  </section>

  <section class="page page--top">
    <div class="illus illus--tile" role="img" aria-label="Illustration of a chat tile with user and call icons" style="left:93px;top:-40px;width:158px;height:88px;background:linear-gradient(135deg,#9ad9f7,#4c9fe3)"></div>
  </section>

  <section class="page page--front">
    <div class="hero-bg"></div>
    <div class="band" style="top:700px;height:110px;transform:rotate(-9deg)"></div>
    <div class="band" style="top:930px;height:120px;transform:rotate(-9deg)"></div>

    <div class="abs logo"><i></i>Zentrik UC</div>
    <nav class="abs nav"><span>HOME</span><span>VOICE ▾</span><span>DATA</span><span>HARDWARE ▾</span><span>SERVICES REQUEST ▾</span><span>STATUS</span><span>SEARCH</span></nav>

    <h1 class="abs hero-title">White-Label Solution for all<br>your Communication Needs</h1>
    <p class="abs hero-sub">Liberating Businesses from Traditional<br>Communications Systems</p>
    <a class="btn" style="left:36px;top:256px">Explore<svg viewBox="0 0 18 8"><path d="M0 4h16M12 1l4 3-4 3" fill="none" stroke="#fff" stroke-width="1"/></svg></a>

    <div class="illus" role="img" aria-label="Illustration of a person on a server tower surrounded by connected communication icons" style="left:374px;top:134px;width:216px;height:216px"></div>
    <div class="dot" style="left:240px;top:65px;width:8px;height:8px"></div>
    <div class="dot" style="left:647px;top:81px;width:14px;height:14px"></div>
    <div class="dot" style="left:330px;top:252px;width:21px;height:21px"></div>
    <div class="dot" style="left:431px;top:291px;width:14px;height:14px"></div>
    <div class="dot dot--b" style="left:334px;top:121px;width:14px;height:14px"></div>
    <div class="dot dot--b" style="left:189px;top:325px;width:9px;height:9px"></div>
    <div class="dot dot--b" style="left:616px;top:336px;width:14px;height:14px;opacity:.6"></div>

    <h2 class="abs section-lead">We have all the components to start and run your<br>own White Label Telco</h2>

    <h2 class="abs feature-title" style="left:89px;top:522px">Cloud IP PBX</h2>
    <p class="abs feature-sub" style="left:89px;top:562px">Multiple IP PBXs on a single instance</p>
    <p class="abs feature-body" style="left:89px;top:590px;width:252px">A Multi-Tenant TenantPBX is able to handle multiple customers (tenants) with a single instance of the software. Even though every customer has a dedicated PBX, they all share the same core engine instance. Using the single instance for all customers cuts down operating costs significantly.</p>
    <a class="btn" style="left:88px;top:668px">See more<svg viewBox="0 0 18 8"><path d="M0 4h16M12 1l4 3-4 3" fill="none" stroke="#fff" stroke-width="1"/></svg></a>
    <div class="illus" role="img" aria-label="Illustration of a cloud with connected network lines" style="left:438px;top:518px;width:168px;height:150px;border-radius:50%"></div>

    <div class="illus illus--tile" role="img" aria-label="Illustration of a chat window with user avatar, call, video and microphone icons" style="left:92px;top:756px;width:158px;height:150px"></div>
    <h2 class="abs feature-title right" style="right:92px;top:743px">Unified Communications</h2>
    <p class="abs feature-sub right" style="right:92px;top:783px">Available on Desktop &amp; Mobile</p>
    <p class="abs feature-body right" style="right:92px;top:811px;width:252px">Zentrik Talk is a Desktop &amp; Mobile Unified Communications application designed to provide business users with a set of features and benefits capable of transforming your company communications system into a real powerhouse.</p>
    <a class="btn" style="left:509px;top:891px">See more<svg viewBox="0 0 18 8"><path d="M0 4h16M12 1l4 3-4 3" fill="none" stroke="#fff" stroke-width="1"/></svg></a>

    <h2 class="abs feature-title" style="left:89px;top:962px">Invoice &amp; Payment Platform</h2>
    <p class="abs feature-sub" style="left:89px;top:1003px">All pieces in one for an assertive management</p>
    <p class="abs feature-body" style="left:89px;top:1031px;width:252px">Ledgera Portal is a fully-featured telecom customer portal, designed for integration with one or many TenantPBX telephony switches. Ledgera Portal has a friendly GUI that enables efficient, automated billing, invoicing and payments, allowing you to spend less time dealing with the administration of your company and more time to SELL!</p>
    <a class="btn" style="left:88px;top:1110px">See more<svg viewBox="0 0 18 8"><path d="M0 4h16M12 1l4 3-4 3" fill="none" stroke="#fff" stroke-width="1"/></svg></a>
    <div class="illus illus--tile" role="img" aria-label="Illustration of a phone with a payment card and dollar signs" style="left:432px;top:982px;width:162px;height:170px;border-radius:18px 60px 0 18px"></div>
  </section>

</div>
</body>
</html>
```